Web Design Project

Hi,
I am building a web based business within the wedding industry and I am looking for someone to design the front page of the website for me as well as the following pages/categroires which all need to be supportive of the front page
The screens will be:
Home
One Stop Reistry
Wedding Deals
Travel/Getaway
Wedding marketplace
Blog
Contact US
A more detailed view of the above is as follows:
1. Home page - be bright and capture an audience
2. Aggregate gift registries ie from key online retailers so people visiting my site can set up a bridal registry from numerous stores all in the one place ie: http://www.harwellmoss.com.au/, http://www.pellow.com.au/, http://www.qtsonix.com.au/ http://www.calvertbrame.com.au/ Something similar to http://www.vowpresentsnow.com.au
3. Aggregate the deal sites to pull all the deals relating to weddings ie: hair and make up, travel, car hire, venue hire, waxing, laser, facials, beauty treatments. Similar to http://www.everybargain.com.au/daily-deals or http://www.yesoffers.com.au/
3. We will have a tab for travel and accommodation which we want to pull the info from Travorna which I believe you can become a member and do so quite easily http://www.travorna.com.au/daily/service/affiliate-program.aspx
4. We want to build like our own tradlo/marketplace within the site where people can list things like their wedding dress, gifts they don’t want or need etc similar to http://www.secondgown.com/
5. A blog tab where we can have blogs/gossip section and build a forum for people to discuss wedding related issues similar to http://www.nuptialnest.com/wedding-forums or http://soontowed.com.au/Forums or gossip like http://www.thestarchatter.com/categories/celebrity-weddings/ The look of this section could be designed to look a bit like a gossip magazine
People need to be able to log in and out of the site and it needs to be able to be connected with pallnet and workloop as well as allowing people to subscribe to a mailing list and unsubscribe if required.
I have done a quick mock-up on powerpoint with what needs to be included but needs a lot of changing. Can be any pictures and what I have attached is not an ide ajust essentials to be on the page.
A good site to give you an idea is http://thevowline.sevenweb.com.au/

```html
<!DOCTYPE html>
<html lang="en">
<head>
<meta charset="utf-8">
<title>Vow Glimmer – Home</title>
<link rel="stylesheet" href="https://fonts.googleapis.com/css2?family=Arimo:wght@400;700&family=Dosis:wght@500&family=Great+Vibes&family=Cormorant+Garamond:ital,wght@1,500&family=Ubuntu:wght@400;500&display=swap">
<style>
:root{
  --topbar:#1d5f78;
  --cream:#fffff0;
  --nav-text:#2f5f8e;
  --contact-label:#9aa4a8;
  --contact-value:#8fc0da;
  --icon-aqua:#8fd0dc;
  --panel:#f3f5f7;
  --card-bg:#fbf9e8;
  --card-border:#e5dfb4;
  --title-blue:#1f4a77;
  --body-text:#4a4a4a;
  --heading:#1e3550;
  --rule:#9ea8b2;
  --login-bg:#e8e8e8;
  --field:#f5f5f5;
  --btn-blue:#1aa4d8;
  --btn-blue-dark:#0b86bf;
  --social-a:#5b7ec6;
  --social-b:#5fb7ea;
  --footer:#6b90bc;
  --footer-text:#e6eef7;
  --logo:#2a8ed0;
}
*{box-sizing:border-box;margin:0;padding:0}
html,body{width:1200px;height:1191px;overflow:hidden}
body{position:relative;font-family:"Arimo",Arial,sans-serif;background:linear-gradient(90deg,#b8c6d3,#dfe5eb 30%,#dfe5eb 70%,#b3c2d0);color:var(--body-text)}
.topbar{position:absolute;left:0;top:0;width:1200px;height:7px;background:var(--topbar)}
.header{position:absolute;left:0;top:7px;width:1200px;height:175px;background:var(--cream)}
.scallop{position:absolute;left:0;top:180px;width:1200px;height:10px;
  background:radial-gradient(circle at 7px 0,var(--cream) 6px,transparent 7px) 0 0/14px 10px repeat-x}
.logo{position:absolute;left:105px;top:44px;font-size:30px;font-weight:700;color:var(--logo);letter-spacing:.5px}
.contact{position:absolute;top:49px;display:flex;gap:12px;align-items:flex-start}
.contact .icon{width:38px;height:38px;border-radius:6px;background:var(--icon-aqua);display:flex;align-items:center;justify-content:center}
.contact small{display:block;font-size:12px;color:var(--contact-label)}
.contact strong{display:block;font-weight:400;font-size:19px;color:var(--contact-value);margin-top:3px}
.nav{position:absolute;top:138px;left:113px;display:flex;font-family:"Dosis",sans-serif;font-size:17px;color:var(--nav-text)}
.nav a{color:inherit;text-decoration:none;margin-right:30px}
.search{position:absolute;left:909px;top:136px;width:183px;height:24px;background:linear-gradient(#dfe3e8,#cdd3da);border:1px solid #c2c8cf;font-size:12px;color:#7a8794;padding:4px 6px}
.search svg{position:absolute;right:4px;top:2px}
.panel{position:absolute;left:91px;top:188px;width:1015px;height:890px;background:var(--panel)}
.card{position:absolute;top:218px;width:284px;height:155px;background:var(--card-bg);border:3px solid var(--card-border);outline:3px solid #fff}
.card h2{position:absolute;left:20px;top:10px;font-family:"Great Vibes",cursive;font-weight:400;font-size:22px;color:var(--title-blue)}
.card .line{position:absolute;left:150px;right:10px;top:24px;border-top:1px solid #bfc8d0}
.card .art{position:absolute;left:12px;top:42px;width:120px;height:80px;border-radius:8px;background:linear-gradient(135deg,#f4f2ec,#d7d9dd)}
.card p{position:absolute;left:142px;top:42px;width:128px;font-size:11px;line-height:16px;text-align:justify}
.card a{position:absolute;left:142px;top:108px;font-family:"Cormorant Garamond",serif;font-style:italic;font-weight:500;font-size:16px;color:var(--title-blue);text-decoration:none}
.photo-frame{position:absolute;left:112px;top:405px;width:671px;height:404px;background:#fff;border-radius:10px;box-shadow:0 0 0 5px #dde3ea}
.photo{position:absolute;left:15px;top:16px;width:645px;height:376px;background:linear-gradient(100deg,#4a4a2a,#7d8a4a 25%,#e9d6b2 45%,#c9906e 65%,#3a2a22 85%,#f2f0ee)}
.login{position:absolute;left:805px;top:405px;width:283px;height:187px;background:var(--login-bg);border-radius:6px;font-family:"Ubuntu",sans-serif}
.login .tab{position:absolute;left:21px;top:-4px;width:176px;height:41px;background:linear-gradient(var(--btn-blue),var(--btn-blue-dark));border-radius:3px 3px 10px 10px;color:#fff;font-size:15px;display:flex;align-items:center;justify-content:center}
.field{position:absolute;left:31px;width:228px;height:34px;background:var(--field);border-radius:14px;box-shadow:inset 0 1px 2px #ccc;font-size:13px;color:#222;padding:9px 10px}
.remember{position:absolute;left:34px;top:152px;font-size:12px;color:#222;display:flex;align-items:center;gap:6px}
.remember i{width:8px;height:8px;border-radius:50%;background:var(--btn-blue)}
.signin{position:absolute;left:168px;top:145px;width:90px;height:28px;border-radius:10px;background:linear-gradient(var(--btn-blue),var(--btn-blue-dark));color:#fff;font-size:13px;display:flex;align-items:center;justify-content:center}
.social{position:absolute;left:810px;width:265px;height:42px;border-radius:21px;color:#fff;font-weight:700;font-size:18px;display:flex;align-items:center;padding-left:16px;gap:14px;border:2px solid #dfe8f3}
.social i{width:18px;height:18px;border-radius:50%;background:#fff}
.social.pallnet{top:611px;background:linear-gradient(var(--social-a),#4a6cb4)}
.social.chirp{top:667px;background:linear-gradient(#7dc8f0,var(--social-b))}
.subscribe{position:absolute;left:805px;top:722px;width:283px;height:84px;background:var(--login-bg)}
.subscribe span{position:absolute;left:13px;top:16px;font-size:12.5px;color:#111}
.subscribe .input{position:absolute;left:9px;top:44px;width:190px;height:32px;border-radius:8px;background:#fff;border:1px solid #d5d5d5}
.subscribe .btn{position:absolute;left:204px;top:44px;width:76px;height:27px;border-radius:5px;background:linear-gradient(var(--btn-blue),var(--btn-blue-dark));color:#111;font-size:12px;display:flex;align-items:center;justify-content:center}
.col{position:absolute;top:851px}
.col h3{font-weight:400;font-size:17px;color:var(--heading);border-top:1px solid var(--rule);border-bottom:1px solid var(--rule);padding:6px;height:32px}
.col p{margin-top:20px;padding:0 6px;width:202px;font-size:11.8px;line-height:17px;text-align:justify}
.footer{position:absolute;left:0;top:1092px;width:1200px;height:99px;background:var(--footer);font-size:11.5px;color:var(--footer-text)}
.footer nav{position:absolute;left:98px;top:16px;display:flex;gap:16px}
.footer .copy{position:absolute;left:1014px;top:16px}
</style>
</head>
<body>
<div class="topbar"></div>
<header class="header">
  <div class="logo">Vow Glimmer</div>
  <div class="contact" style="left:434px">
    <div class="icon"><svg width="20" height="22" viewBox="0 0 20 22"><path d="M5 1h4l1 5-3 2c1 3 3 5 6 7l2-3 5 1v4c0 2-2 3-4 3C8 20 1 13 1 5 1 3 3 1 5 1z" fill="#fff"/></svg></div>
    <div><small>Call us now</small><strong>015550147</strong></div>
  </div>
  <div class="contact" style="left:611px">
    <div class="icon"><svg width="24" height="20" viewBox="0 0 24 20"><path d="M3 2h18c1 0 2 1 2 2v8c0 1-1 2-2 2H10l-5 4v-4H3c-1 0-2-1-2-2V4c0-1 1-2 2-2z" fill="#fff"/></svg></div>
    <div><small>Chat with us</small><strong>Click to Live Chat</strong></div>
  </div>
  <div class="contact" style="left:840px">
    <div class="icon"><svg width="24" height="20" viewBox="0 0 24 20"><path d="M3 2h18c1 0 2 1 2 2v8c0 1-1 2-2 2H10l-5 4v-4H3c-1 0-2-1-2-2V4c0-1 1-2 2-2z" fill="#fff"/></svg></div>
    <div><small>Get a quote</small><strong>Submit request here</strong></div>
  </div>
  <nav class="nav">
    <a href="#">Home</a><a href="#">One Stop Registry</a><a href="#">Wedding Deals</a><a href="#">Travel/Accomodation Gateway</a><a href="#">Weding Marketplace</a>
  </nav>
  <div class="search">Search<svg width="20" height="18" viewBox="0 0 20 18"><circle cx="8" cy="8" r="6" fill="#eef3f7" stroke="#6b7c8c" stroke-width="1.5"/><path d="M12 12l6 5" stroke="#6b7c8c" stroke-width="2"/></svg></div>
</header>
<div class="scallop"></div>

<main class="panel"></main>

<section class="card" style="left:117px">
  <h2>Wedding Deals</h2><div class="line"></div>
  <div class="art" role="img" aria-label="Rolled paper scroll illustration"></div>
  <p>Lorem Ipsum is simply dummy text of the printing and typesetting industry.</p>
  <a href="#">Find your deal</a>
</section>
<section class="card" style="left:456px">
  <h2>Gossip | Editorial</h2><div class="line" style="left:175px"></div>
  <div class="art" role="img" aria-label="Parchment scroll illustration" style="background:linear-gradient(135deg,#fbeee2,#e8c9b6)"></div>
  <p>Lorem Ipsum is simply dummy text of the printing and typesetting industry.</p>
  <a href="#">Find more</a>
</section>
<section class="card" style="left:793px">
  <h2>Booking Engine</h2><div class="line" style="left:160px"></div>
  <div class="art" role="img" aria-label="Blue pointing hand cursor illustration" style="background:linear-gradient(135deg,#3fa6e6,#0c4f9c)"></div>
  <p>Lorem Ipsum is simply dummy text of the printing and typesetting industry.</p>
  <a href="#">Find your package</a>
</section>

<div class="photo-frame"><div class="photo" role="img" aria-label="Photo of a bride and groom embracing outdoors with champagne glasses"></div></div>

<form class="login">
  <div class="tab">Login Now / Register</div>
  <div class="field" style="top:59px">Username</div>
  <div class="field" style="top:103px">*********</div>
  <div class="remember"><i></i>Remember Me</div>
  <div class="signin">Sign-in</div>
</form>

<div class="social pallnet"><i></i>Sign in with pallnet</div>
<div class="social chirp"><i></i>Sign in with chirpwire</div>

<div class="subscribe"><span>Subscribe to our mailing list</span><div class="input"></div><div class="btn">Subscribe</div></div>

<section class="col" style="left:110px;width:201px"><h3>ABOUT US</h3><p>Lorem Ipsum is simply dummy text of the printing and typesetting industry. Lorem Ipsum has been the industry's standard dummy text ever since the 1500s, when an unknown printer took a galley of type and scrambled it to make a type specimen book.</p></section>
<section class="col" style="left:362px;width:225px"><h3>CUSTOMER SERVICE</h3><p>Lorem Ipsum is simply dummy text of the printing and typesetting industry. Lorem Ipsum has been the industry's standard dummy text ever since the 1500s, when an unknown printer took a galley of type and scrambled it to make a type specimen book.</p></section>
<section class="col" style="left:631px;width:205px"><h3>TESTIMONIALS</h3><p>Lorem Ipsum is simply dummy text of the printing and typesetting industry. Lorem Ipsum has been the industry's standard dummy text ever since the 1500s, when an unknown printer took a galley of type and scrambled it to make a type specimen book.</p></section>
<section class="col" style="left:873px;width:219px"><h3>LATEST BLOG POSTS</h3><p>Lorem Ipsum is simply dummy text of the printing and typesetting industry. Lorem Ipsum has been the industry's standard dummy text ever since the 1500s, when an unknown printer took a galley of type and scrambled it to make a type specimen book.</p></section>

<footer class="footer">
  <nav><span>About Vow Glimmer</span><span>Advertise with us</span><span>Contact Us</span><span>Term &amp; Conditions</span><span>Privacy Policy</span></nav>
  <span class="copy">Copyright</span>
</footer>
</body>
</html>
```